Video production company website

BrightWave Studios is a video and photography production company serving many Fortune 500 clients traveling to Hawaii and International Destinations. Our primary focus is the Corporate and Incentive group market, and offer both photography and video services. In addition, we also create custom marketing, sales, art, and real estate productions.

Target Market(s)

Corporate Incentive Travel Groups

Industry/Entity Type

Videography

Number of Pages Required

4 page

Requirements
Must have
• see doc with content. This will ultimately be needed to be a wordpress design so we can update ourselves.
Nice to have
• sleek design, professional, cutting edge, modern
Should not have
• too much Hawaii Feel, some ok but we do travel international

```html
<!DOCTYPE html>
<html lang="en">
<head>
<meta charset="utf-8">
<title>Contact Us – BrightWave Studios</title>
<link href="https://fonts.googleapis.com/css2?family=Lato:wght@300;400;700&family=Playfair+Display:wght@400&display=swap" rel="stylesheet">
<style>
  :root {
    --ink: #0d0d0d;
    --white: #ffffff;
    --red: #e8102a;
    --yellow: #f2c21a;
    --teal: #12b8a6;
    --cyan: #27e6e0;
    --shade-1: #1a1a1a;
    --shade-2: #3a3a3a;
    --shade-3: #8a8a8a;
  }
  * { margin: 0; padding: 0; box-sizing: border-box; }
  html, body { width: 1200px; height: 619px; overflow: hidden; background: var(--ink); }
  .page {
    position: relative; width: 1200px; height: 619px; overflow: hidden;
    font-family: "Lato", sans-serif; color: var(--white);
  }
  .backdrop {
    position: absolute; inset: 0;
    background:
      linear-gradient(90deg, rgba(13,13,13,0.9) 0%, rgba(13,13,13,0.55) 45%, rgba(13,13,13,0) 75%),
      linear-gradient(160deg, var(--shade-1) 0%, var(--shade-2) 45%, var(--shade-3) 80%, #b5b5b5 100%);
  }
  .menu-toggle { position: absolute; left: 38px; top: 34px; width: 22px; }
  .page-title {
    position: absolute; left: 84px; top: 70px;
    font-family: "Playfair Display", serif; font-weight: 400; font-size: 88px;
    line-height: 1; letter-spacing: -1px;
    text-shadow: -3px 0 0 var(--cyan), 3px 0 0 var(--red);
  }
  .brand { position: absolute; left: 940px; top: 20px; width: 240px; text-align: center; }
  .brand-mark {
    width: 128px; height: 128px; margin: 0 auto; border-radius: 50%;
    background: var(--white);
  }
  .brand-name {
    margin-top: 16px; font-size: 15px; font-weight: 700; letter-spacing: 1px;
    color: var(--white);
  }
  .accent-bands { position: absolute; left: 0; top: 181px; }
  .section-heading {
    position: absolute; font-weight: 300; font-size: 36px; line-height: 1; letter-spacing: 0.5px;
  }
  .address-heading { left: 104px; top: 214px; }
  .message-heading { left: 642px; top: 214px; }
  .address {
    position: absolute; left: 104px; top: 263px;
    font-style: normal; font-size: 10.5px; line-height: 17.6px;
  }
  .sign-off {
    position: absolute; left: 102px; top: 402px; width: 380px;
    font-weight: 300; font-size: 21.5px; line-height: 32px;
  }
  .quick-form { position: absolute; left: 560px; top: 272px; width: 360px; }
  .field { display: flex; align-items: flex-end; height: 39px; }
  .field:first-child { height: 20px; }
  .field-label { width: 94px; font-size: 10px; padding-bottom: 4px; }
  .field-line { width: 256px; height: 1px; border-bottom: 1px solid var(--white); }
  .send-button {
    position: absolute; left: 801px; top: 490px; width: 113px; height: 35px;
    background: var(--white); color: var(--ink); border: 0; border-radius: 6px;
    font-family: "Lato", sans-serif; font-weight: 700; font-size: 9.5px;
    box-shadow: -2px 0 0 var(--cyan), 2px 1px 0 var(--red);
  }
  .site-footer {
    position: absolute; left: 24px; top: 576px; font-size: 10.5px; line-height: 16px;
  }
</style>
</head>
<body>
<div class="page">
  <div class="backdrop" role="img" aria-label="Black and white photo of a smiling passenger in a small propeller aircraft cockpit"></div>

  <svg class="menu-toggle" viewBox="0 0 22 14" aria-label="Menu">
    <rect x="0" y="0" width="22" height="2" fill="#fff"/>
    <rect x="0" y="6" width="22" height="2" fill="#fff"/>
    <rect x="0" y="12" width="22" height="2" fill="#fff"/>
  </svg>

  <h1 class="page-title">CONTACT US</h1>

  <div class="brand">
    <div class="brand-mark"></div>
    <div class="brand-name">BRIGHTWAVE STUDIOS</div>
  </div>

  <svg class="accent-bands" width="76" height="312" viewBox="0 0 76 312" aria-hidden="true">
    <rect x="-10" y="0" width="85" height="311" rx="5" fill="var(--teal)"/>
    <rect x="-10" y="0" width="61" height="311" rx="5" fill="var(--yellow)"/>
    <rect x="-10" y="0" width="30" height="311" rx="5" fill="var(--red)"/>
  </svg>

  <h2 class="section-heading address-heading">ADDRESS</h2>
  <address class="address">
    BRIGHTWAVE STUDIOS, LLC<br>
    P.O. BOX 412-870<br>
    WAILEA HI 96700<br>
    (808) 555.0142 PH<br>
    (808) 555.0197 FAX
  </address>

  <p class="sign-off">WE LOOK FORWARD TO HEARING FROM YOU.&nbsp; ALOHA, MARCUS LANE-PRESIDENT.</p>

  <h2 class="section-heading message-heading">QUICK MESSAGE</h2>
  <div class="quick-form">
    <div class="field"><span class="field-label">NAME</span><span class="field-line"></span></div>
    <div class="field"><span class="field-label">COMPANY INFO</span><span class="field-line"></span></div>
    <div class="field"><span class="field-label">PHONE</span><span class="field-line"></span></div>
    <div class="field"><span class="field-label">EMAIL</span><span class="field-line"></span></div>
    <div class="field"><span class="field-label">MESSAGE</span><span class="field-line"></span></div>
  </div>
  <button class="send-button" type="button">SEND MESSAGE</button>

  <footer class="site-footer">
    <div>•&nbsp; ▸&nbsp; T &amp; C / PRIVACY</div>
    <div>BRIGHTWAVESTUDIOS © 2016. ALL RIGHTS RESERVED.</div>
  </footer>
</div>
</body>
</html>
```